Plumbing and heating business card design

i need a new business card for the company i work for called Dr. Brightwell. It is a plumbing and heating company that has been operating for over 30 years. We are not like these big plumbing companies that have ways to charge the customer as much as possible. Our company does only what is necessary and what is needed to do the job right the first time without the high cost. we are a neighborhood business which kind of explains why we don't charge customers through the roof. I would like to see a design with a nice background anything but just plain white. maybe like a light blue at the top of the design. on the back of the card i would like it to say " T. Vantelli's Dr. Brightwell". maybe add some color to the lettering on the front of the card for example blue font for plumbing and red font for heating. raised print. im sure Cardmerro designers will make it look good. The final design should help spread a good word about our company and help grow business.

Industry/Entity Type

Business

Contact Information for Business Card

Dr. Brightwell, Plumbing & heating, Daniel Hosker, Northeast District Operations manager, 4827 Pellworth st., Office:(555)-782-1093, doctorbrightwell@pipemailer.example

Requirements
Must have
• raised print finish and a nice sturdy feel.

```html
<!DOCTYPE html>
<html lang="en">
<head>
<meta charset="utf-8">
<title>Dr. Brightwell – Business Card</title>
<link href="https://fonts.googleapis.com/css2?family=Montserrat:wght@400;500;600;700&display=swap" rel="stylesheet">
<style>
  :root {
    --canvas-bg: #e6e2de;
    --card-bg: #000000;
    --silver: #c7c7c7;
    --silver-dark: #9a9a9a;
    --white: #ffffff;
    --brand-blue: #2c4ea0;
    --pin-blue: #2f5db8;
    --brand-red: #d9302a;
    --divider: #4a4a4a;
    --mark-blue: #2d7fae;
  }
  * { margin: 0; padding: 0; box-sizing: border-box; }
  html, body {
    width: 1200px;
    height: 1000px;
    overflow: hidden;
    background: var(--canvas-bg);
    font-family: "Montserrat", Arial, sans-serif;
  }
  .canvas { position: relative; width: 1200px; height: 1000px; }

  .card {
    position: absolute;
    width: 620px;
    height: 340px;
    background: var(--card-bg);
    box-shadow: 0 8px 18px rgba(0,0,0,0.25);
  }

  /* Back of card */
  .card-back { left: 110px; top: 110px; }
  .card-back .lockup {
    position: absolute;
    left: 0; right: 0; top: 78px;
    display: flex; flex-direction: column; align-items: center;
    color: var(--silver);
    font-weight: 700;
  }
  .lockup .brand-dot {
    width: 58px; height: 58px; border-radius: 50%;
    background: var(--silver-dark);
    margin-bottom: 22px;
  }
  .card-back .owner { font-size: 20px; line-height: 1; font-weight: 500; }
  .card-back .brand-name { font-size: 42px; line-height: 1.1; }
  .card-back .tagline { font-size: 20px; line-height: 1.1; font-weight: 500; }

  /* Front of card */
  .card-front { left: 412px; top: 528px; height: 360px; }
  .card-front .brand-side {
    position: absolute;
    left: 0; top: 0; width: 296px; height: 100%;
    display: flex; flex-direction: column; align-items: center; justify-content: center;
    padding-top: 30px;
  }
  .card-front .brand-dot {
    width: 50px; height: 50px; border-radius: 50%;
    background: var(--mark-blue);
    margin-bottom: 28px;
  }
  .card-front .brand-name {
    color: var(--silver);
    font-weight: 700;
    font-size: 30px;
    line-height: 1;
    white-space: nowrap;
  }
  .card-front .tagline {
    font-size: 14px; font-weight: 500; margin-top: 4px;
  }
  .tagline .plumbing { color: var(--brand-blue); }
  .tagline .heating { color: var(--brand-red); }
  .card-back .tagline span { color: var(--silver); }

  .card-front .divider {
    position: absolute; left: 296px; top: 62px; width: 1px; height: 238px;
    background: var(--divider);
  }
  .contact-side { position: absolute; left: 322px; top: 88px; right: 20px; }
  .person-name { color: var(--white); font-size: 22px; font-weight: 500; line-height: 1.1; }
  .person-title { color: var(--brand-blue); font-size: 12px; font-weight: 500; margin-top: 4px; }
  .contact-list { list-style: none; margin-top: 50px; }
  .contact-list li {
    display: flex; align-items: center; gap: 12px;
    color: var(--white); font-size: 13px; height: 31px;
  }
  .contact-list svg { width: 26px; height: 26px; flex-shrink: 0; }
</style>
</head>
<body>
<main class="canvas">

  <section class="card card-back" aria-label="Back of business card">
    <div class="lockup">
      <div class="brand-dot"></div>
      <span class="owner">T. Vantelli's</span>
      <span class="brand-name">Dr. Brightwell</span>
      <span class="tagline"><span>Plumping and HVAC</span></span>
    </div>
  </section>

  <section class="card card-front" aria-label="Front of business card">
    <div class="brand-side">
      <div class="brand-dot"></div>
      <span class="brand-name">Dr. Brightwell</span>
      <span class="tagline"><span class="plumbing">Plumping</span> <span class="plumbing">and</span> <span class="heating">HVAC</span></span>
    </div>
    <div class="divider"></div>
    <div class="contact-side">
      <p class="person-name">Daniel Hosker</p>
      <p class="person-title">Northeast District Operations Manager</p>
      <ul class="contact-list">
        <li>
          <svg viewBox="0 0 26 26" aria-hidden="true">
            <path d="M13 2a8 8 0 0 0-8 8c0 6 8 14 8 14s8-8 8-14a8 8 0 0 0-8-8z" fill="var(--pin-blue)"/>
            <circle cx="13" cy="10" r="3.2" fill="var(--brand-red)"/>
          </svg>
          4827 Pellworth st.
        </li>
        <li>
          <svg viewBox="0 0 26 26" aria-hidden="true">
            <circle cx="13" cy="13" r="11" fill="none" stroke="var(--pin-blue)" stroke-width="2"/>
            <path d="M8.5 8.2l2.3-1 1.6 3.2-1.4 1.2c.7 1.6 1.8 2.7 3.4 3.4l1.2-1.4 3.2 1.6-1 2.3c-5 0-9.3-4.3-9.3-9.3z" fill="var(--brand-red)"/>
          </svg>
          (555)-782-1093
        </li>
        <li>
          <svg viewBox="0 0 26 26" aria-hidden="true">
            <rect x="2" y="6" width="22" height="16" rx="1.5" fill="var(--pin-blue)"/>
            <path d="M2 7l11 8 11-8" fill="none" stroke="var(--brand-red)" stroke-width="2"/>
          </svg>
          doctorbrightwell@pipemailer.example
        </li>
      </ul>
    </div>
  </section>

</main>
</body>
</html>
```